Webdesign für Automotive Engineering Webpage
Automotive Engineering - Main focus is Software Development & Embedded systems for the Automotive industry.
Like as HMI, ADAS, ECU
See Logo (PDF), example --> https://www.brantlex.com/de/de (competetor)

```html
<!DOCTYPE html>
<html lang="de">
<head>
<meta charset="utf-8">
<title>VALTRIX – Automotive Engineering &amp; Consulting Solutions</title>
<link href="https://fonts.googleapis.com/css2?family=Lato:wght@400;700&family=Poppins:ital,wght@0,600;1,800&display=swap" rel="stylesheet">
<style>
:root{
  --navy:#0c2b5c;
  --navy-deep:#08214a;
  --red:#e4222b;
  --white:#ffffff;
  --ink:#2b2f3a;
  --muted:#6b7280;
  --line:#e5e7eb;
}
*{box-sizing:border-box;margin:0;padding:0}
html,body{width:1200px;height:4368px;overflow:hidden}
body{font-family:"Lato",sans-serif;color:var(--ink);background:var(--white);position:relative}
.abs{position:absolute}
.display{font-family:"Poppins",sans-serif;font-weight:800;font-style:italic;line-height:1.18}
.accent{color:var(--red)}
.body-text p{font-size:12.5px;line-height:1.5;margin-bottom:17px}

/* header */
.menu-tile{left:0;top:0;width:83px;height:124px;background:var(--red);display:flex;align-items:center;justify-content:center}
.menu-tile span{display:block;width:34px;height:3px;background:var(--white);margin:6px 0}
.brand{display:flex;align-items:center;gap:10px;font-family:"Poppins",sans-serif;font-weight:600;font-size:30px;letter-spacing:2px;color:var(--navy)}
.brand i{display:block;width:12px;height:12px;border-radius:50%;background:var(--red)}
.header-brand{left:0;width:1200px;top:40px;justify-content:center}

/* sidebar */
.sidebar{left:0;top:124px;width:83px;height:625px;background:var(--navy-deep)}
.sidebar svg{display:block;margin:0 auto}
.side-icons{padding-top:42px;display:flex;flex-direction:column;gap:44px}
.side-brand{position:absolute;left:22px;top:390px;writing-mode:vertical-rl;transform:rotate(180deg);color:var(--white);font-family:"Poppins",sans-serif;font-weight:600;font-size:22px;letter-spacing:2px}

/* hero */
.hero{left:83px;top:124px;width:1117px;height:625px;background:linear-gradient(160deg,#3b5f8e 0%,#1c3d6d 45%,#0a2450 100%)}
.hero-title{left:125px;top:510px;font-size:49px;color:var(--white)}
.btn{display:inline-block;background:var(--red);color:var(--white);font-family:"Lato",sans-serif;font-size:12px;letter-spacing:1.5px;text-transform:uppercase}
.hero-btn{left:127px;top:659px;width:198px;height:36px;line-height:36px;text-align:center}

/* originate */
.origin-photo{left:0;top:749px;width:380px;height:465px;background:linear-gradient(135deg,#233f66,#3f6e9c 55%,#c9d6e3)}
.origin-text{left:442px;top:815px;width:600px}
.section-title{font-size:30px;color:var(--navy)}

/* who */
.who{left:0;top:1214px;width:712px;height:545px;background:var(--navy)}
.who-photo{left:712px;top:1214px;width:488px;height:545px;background:linear-gradient(160deg,#2f4f72,#55708c 50%,#8a97a6)}
.who-text{left:83px;top:1278px;width:550px;color:var(--white)}

/* services */
.services-title{left:83px;top:1822px}
.service{width:258px;height:256px}
.service .pic{position:absolute;inset:0}
.service .cap{position:absolute;left:0;right:0;bottom:0;height:82px;background:rgba(228,34,43,.85);color:var(--white);padding:14px 14px}
.service h3{font-size:14px;font-weight:700;margin-bottom:4px}
.service p{font-size:12px;line-height:1.4;opacity:.9}
.s1{left:171px;top:1936px;box-shadow:0 6px 18px rgba(0,0,0,.2)}
.s1 .pic{background:linear-gradient(135deg,#1c2a44,#3a4b6a 55%,#c8532a)}
.s2{left:471px;top:2009px}
.s2 .pic{background:linear-gradient(135deg,#d8d6d0,#8a7260 60%,#5a6470)}
.s3{left:771px;top:1936px}
.s3 .pic{background:linear-gradient(135deg,#e6e6e6,#8b8f93 55%,#3d3a36)}

/* focus */
.focus-photo{left:0;top:2329px;width:480px;height:590px;background:linear-gradient(135deg,#e8ecef,#a9b6c2 50%,#4d5d6e)}
.focus{left:480px;top:2329px;width:720px;height:590px;background:var(--navy)}
.focus-text{left:558px;top:2388px;width:556px;color:var(--white)}

/* jobs */
.jobs-title{left:83px;top:2984px}
.jobs-box{left:83px;top:3068px;width:1034px;height:456px;background:var(--white);box-shadow:0 4px 22px rgba(0,0,0,.14)}
.jobs-box p{margin-top:92px;text-align:center;font-family:"Poppins",sans-serif;font-weight:600;font-size:25px;color:var(--navy)}

/* contact */
.contact{left:0;top:3600px;width:1200px;height:454px;background:var(--navy)}
.contact-label{left:100px;top:3677px;font-size:11px;letter-spacing:2px;color:#9fb0cc;text-transform:uppercase}
.contact-title{left:100px;top:3710px;width:500px;font-size:30px;color:var(--white)}
.contact-intro{left:100px;top:3878px;width:360px;font-size:12.5px;line-height:1.45;color:var(--white)}
.field{left:653px;width:464px;height:37px;background:var(--white);font-size:12px;color:#9aa3b2;padding:11px 12px}
.send{left:653px;top:3934px;width:181px;height:37px;line-height:37px;text-align:center}

/* footer */
.footer-brand{left:100px;top:4140px;font-size:28px}
.socials{left:100px;top:4222px;display:flex;gap:16px}
.socials span{display:block;width:20px;height:20px;background:var(--navy)}
.fcol{top:4110px}
.fcol h4{font-size:13px;font-weight:700;color:var(--navy);margin-bottom:14px}
.fcol li{list-style:none;font-size:12.5px;color:var(--navy);margin-bottom:11px}
.contact-list li{display:flex;gap:10px;font-size:11px;line-height:1.5;margin-bottom:6px}
.contact-list svg{flex:none;margin-top:2px}
.bottom-bar{left:0;top:4322px;width:1200px;height:46px;background:var(--red);color:var(--white);font-size:11px;padding:0 83px;display:flex;justify-content:space-between;align-items:center}
</style>
</head>
<body>

<header>
  <div class="abs menu-tile" aria-label="Menü"><div><span></span><span></span><span></span></div></div>
  <div class="abs brand header-brand"><i></i>VALTRIX</div>
</header>

<nav class="abs sidebar">
  <div class="side-icons">
    <svg width="22" height="22" viewBox="0 0 24 24" fill="none" stroke="#fff" stroke-width="2.4"><circle cx="10" cy="10" r="6"/><path d="M15 15l6 6"/></svg>
    <svg width="24" height="24" viewBox="0 0 24 24" fill="none" stroke="#fff" stroke-width="2"><circle cx="12" cy="12" r="9"/><path d="M3 12h18M12 3c3 3 3 15 0 18M12 3c-3 3-3 15 0 18"/></svg>
    <svg width="22" height="22" viewBox="0 0 24 24" fill="#fff"><path d="M6.6 10.8c1.4 2.8 3.8 5.1 6.6 6.6l2.2-2.2c.3-.3.7-.4 1-.2 1.1.4 2.3.6 3.6.6.6 0 1 .4 1 1V20c0 .6-.4 1-1 1C10.6 21 3 13.4 3 4c0-.6.4-1 1-1h3.5c.6 0 1 .4 1 1 0 1.3.2 2.5.6 3.6.1.3 0 .7-.2 1z"/></svg>
    <svg width="22" height="22" viewBox="0 0 24 24" fill="none" stroke="#fff" stroke-width="2"><rect x="6" y="3" width="15" height="15"/><path d="M3 7v14h14M9 8h9M9 12h9M9 15h6"/></svg>
  </div>
  <div class="side-brand">VALTRIX</div>
</nav>

<section>
  <div class="abs hero" role="img" aria-label="Foto: Ingenieure arbeiten nachts an Bildschirmen mit technischen Zeichnungen"></div>
  <h1 class="abs display hero-title">Automotive Engineering<br>&amp; Consulting Solutions</h1>
  <a class="abs btn hero-btn">Zur Projektübersicht</a>
</section>

<section>
  <div class="abs origin-photo" role="img" aria-label="Foto: Ingenieurin vor Monitoren mit Fahrzeugmodell"></div>
  <div class="abs origin-text body-text">
    <h2 class="display section-title" style="margin-bottom:36px">Originate in <span class="accent">Engineering</span></h2>
    <p>Holmberg Recruitment vereint in sich 25 Jahre Branchen- und Projekterfahrung vom Freelance Ingenieur bis zum Task Force Manager in den Branchen Automotive, Schienenfahrzeuge, Luft- und Raumfahrt, Rüstung und Informationstechnologie.</p>
    <p>Firmengründer und Geschäftsführer Jonas Holmberg kennt die Industrie seit über zwei Jahrzehnten, in denen er in Positionen als IT Entwicklungsingenieur, Experte für Geodaten und rund um das Thema autonomes Fahren und Fahrassistenzsysteme, bis zum CIO und Task Force Manager bei fast allen wichtigen OEMs und Tier1s des Automotive Sektors und anderer Schlüsselindustrien Erfahrungen sammeln konnte.</p>
    <p>Wie der Firmengründer, so verfügen auch alle maßgeblichen Mitarbeiter bei Holmberg Recruitment über diese Double Qualification – wir sprechen Ihre Sprache und wissen, wo Ihr Bedarf liegt, kennen Ihre Abläufe und Prozesse, sind aus eigener Erfahrung heraus im Geschäft.</p>
  </div>
</section>

<section>
  <div class="abs who"></div>
  <div class="abs who-photo" role="img" aria-label="Foto: lächelnder junger Ingenieur im Kontrollraum"></div>
  <div class="abs who-text body-text">
    <h2 class="display section-title" style="color:var(--white);margin-bottom:36px">Wer wir <span class="accent">sind</span></h2>
    <p>Holmberg Recruitment vereint in sich 25 Jahre Branchen- und Projekterfahrung vom Freelance Ingenieur bis zum Task Force Manager in den Branchen Automotive, Schienenfahrzeuge, Luft- und Raumfahrt, Rüstung und Informationstechnologie.</p>
    <p>Firmengründer und Geschäftsführer Jonas Holmberg kennt die Industrie seit über zwei Jahrzehnten, in denen er in Positionen als IT Entwicklungsingenieur, Experte für Geodaten und rund um das Thema autonomes Fahren und Fahrassistenzsysteme, bis zum CIO und Task Force Manager bei fast allen wichtigen OEMs und Tier1s des Automotive Sektors und anderer Schlüsselindustrien Erfahrungen sammeln konnte.</p>
    <p>Wie der Firmengründer, so verfügen auch alle maßgeblichen Mitarbeiter bei Holmberg Recruitment über diese Double Qualification. Sie sprechen mit Fachleuten und Kollegen, nicht mit reinen Recruitern!</p>
    <p>Wir wissen, wo der Bedarf unserer Kunden liegt, kennen deren Abläufe und Prozesse, sind aus eigener Erfahrung heraus im Geschäft.</p>
  </div>
</section>

<section>
  <h2 class="abs display section-title services-title">Unsere <span class="accent">Leistungen</span></h2>
  <article class="abs service s1">
    <div class="pic" role="img" aria-label="Bild: Hand berührt digitale Engineering-Symbole"></div>
    <div class="cap"><h3>Full Service Engineering</h3><p>Übernahme kompletter R&amp;D Projekte als Fremdleistung</p></div>
  </article>
  <article class="abs service s2">
    <div class="pic" role="img" aria-label="Foto: Berater im Gespräch am Schreibtisch"></div>
    <div class="cap"><h3>Premium Recruiting</h3><p>Vermittlung bis hin zum Onboarding von Freelancern und Festangestellten</p></div>
  </article>
  <article class="abs service s3">
    <div class="pic" role="img" aria-label="Foto: Ingenieur mit Brille im Büro"></div>
    <div class="cap"><h3>Arbeitnehmerüberlassung</h3><p>Automotive R&amp;D Experten und Ingenieure in Zeitarbeit</p></div>
  </article>
</section>

<section>
  <div class="abs focus-photo" role="img" aria-label="Foto: Ingenieur arbeitet am Rechner mit CAD-Modell"></div>
  <div class="abs focus"></div>
  <div class="abs focus-text body-text">
    <h2 class="display section-title" style="color:var(--white);margin-bottom:36px">Konzentrieren Sie sich auf Ihre<br><span class="accent">Kernkompetenzen</span></h2>
    <p>Ihr Wissen, Ihre Erfahrung und Ihr Können sind wertvolle Assets. Sie brauchen nur noch die richtigen Verbindungen, um eine finanziell wie emotional befriedigende Arbeit daraus zu kreieren. Genau für letzteres können Sie uns ansprechen. Wir kennen Ihre Situation und Ihre Wünsche aus eigenen, langjährigen Erfahrungen, denn wir kommen aus dem IT- und Engineering-Bereich. Wir haben selbst als Freelancer in Automotive und anderen Schlüsselindustrien gearbeitet und wissen, was Sie suchen!</p>
    <p>Wir vermitteln Sie als Freelancer oder festangestellt projekt- oder zeitbezogen an Ihre Wunschpartner in der Industrie. Wenn Sie in einem festen Arbeitsverhältnis oder im Rahmen einer Arbeitnehmerüberlassung angestellt werden wollen, können Sie uns ebenfalls ansprechen. Wir arbeiten zudem international mit den führenden OEMs, Tier-1 und Tier-2 Unternehmen der Automobilindustrie zusammen.</p>
    <p>Aber bevor Sie uns gleich Ihre Unterlagen schicken, nehmen Sie kurz Kontakt mit uns auf, damit von Anfang an alles passt. Unsere Arbeit lebt von Effektivität und Effizienz und wir wollen weder Ihre, noch die Zeit unserer Kunden mit offenen Fragen oder gar Nachbesserungen verschwenden!</p>
    <p>Sie wollen sich initativ bewerben? Schicken Sie uns bitte Ihre Unterlagen an<br>cv@holmberg-recruit.de</p>
  </div>
</section>

<section>
  <h2 class="abs display section-title jobs-title">Offene <span class="accent">Stellen</span></h2>
  <div class="abs jobs-box"><p>Hier das Add-in aus Karrierenetz einfügen für Vakanzen und Ausschreibungen</p></div>
</section>

<section>
  <div class="abs contact"></div>
  <div class="abs contact-label">Holmberg Recruitment GmbH</div>
  <h2 class="abs display contact-title">Sie suchen Spezialisten für eine bestimmte Aufgabe, oder möchten mit uns in Kontakt treten?</h2>
  <p class="abs contact-intro">Senden Sie uns zum Beispiel Ihre Anforderungen und wir kommen mit passenden Profilen auf Sie zu, oder nehmen Sie einfach mit uns Kontakt auf und erfahren was wir für Sie tun können.</p>
  <div class="abs field" style="top:3704px">Name*</div>
  <div class="abs field" style="top:3761px">E-Mail*</div>
  <div class="abs field" style="top:3819px">Telefonnummer</div>
  <div class="abs field" style="top:3876px">Ort/PLZ*</div>
  <a class="abs btn send">Anfrage absenden</a>
</section>

<footer>
  <div class="abs brand footer-brand"><i></i>VALTRIX</div>
  <div class="abs socials" aria-label="Soziale Netzwerke"><span></span><span></span><span></span><span></span></div>
  <div class="abs fcol" style="left:386px">
    <h4>Navigation</h4>
    <ul><li>Über uns</li><li>Unsere Leistungen</li><li>Bewerber</li><li>Offene Stellen</li><li>Kontakt</li></ul>
  </div>
  <div class="abs fcol" style="left:637px">
    <h4>Kundenservice</h4>
    <ul><li>Registrieren</li><li>Impressum</li><li>Datenschutz</li></ul>
  </div>
  <div class="abs fcol" style="left:888px">
    <h4>Adresse &amp; Kontakt</h4>
    <ul class="contact-list">
      <li><svg width="14" height="14" viewBox="0 0 24 24" fill="#b8bfcc"><path d="M12 2a7 7 0 0 0-7 7c0 5 7 13 7 13s7-8 7-13a7 7 0 0 0-7-7zm0 9.5A2.5 2.5 0 1 1 12 6.5a2.5 2.5 0 0 1 0 5z"/></svg><span>Lindenstraße 4<br>D - 12345 Musterfeld (OT Nord)</span></li>
      <li><svg width="14" height="14" viewBox="0 0 24 24" fill="#b8bfcc"><path d="M6.6 10.8c1.4 2.8 3.8 5.1 6.6 6.6l2.2-2.2c.3-.3.7-.4 1-.2 1.1.4 2.3.6 3.6.6.6 0 1 .4 1 1V20c0 .6-.4 1-1 1C10.6 21 3 13.4 3 4c0-.6.4-1 1-1h3.5c.6 0 1 .4 1 1 0 1.3.2 2.5.6 3.6.1.3 0 .7-.2 1z"/></svg><span>+49 (0)1234 -567 89 01</span></li>
      <li><svg width="14" height="14" viewBox="0 0 24 24" fill="#b8bfcc"><path d="M6 3h12v5H6zM3 9h18v9h-3v3H6v-3H3zm5 7v3h8v-3z"/></svg><span>+49 (0)1234 -567 89 02</span></li>
      <li><svg width="14" height="14" viewBox="0 0 24 24" fill="#b8bfcc"><path d="M3 5h18v14H3zm2 2v.5l7 4.5 7-4.5V7z"/></svg><span>office@holmberg-recruit.de<br>D-U-N-S Nr. 123456789</span></li>
    </ul>
  </div>
  <div class="abs bottom-bar"><span>© 2020 valtrix.com | All rights reserved.</span><span>TermsOfUse &nbsp;Privacy</span></div>
</footer>

</body>
</html>
```